Design a double sided business card

We are looking for a clean, eye-catching, and contemporary design that enhances the brand and presents a premium, professional image. Our preference is for a brown card with black gloss detailing and embossed elements; however, we are open to creative input and design suggestions that best achieve a strong visual impact.

Please see the attached existing business card for reference. We use both black and brown colours consistently across our branding.

On sample provided

```html
<!DOCTYPE html>
<html lang="en">
<head>
<meta charset="utf-8">
<title>Kelmont business card</title>
<link rel="stylesheet" href="https://fonts.googleapis.com/css2?family=Lato:wght@400;700&family=Playfair+Display:wght@400&display=swap">
<style>
  :root {
    --backdrop: #2a2a2a;
    --card: #1b1b1b;
    --gold: #c9b497;
    --gold-dim: #a8967d;
    --gloss-light: #8a8a8a;
    --gloss-dark: #141414;
  }
  * { box-sizing: border-box; margin: 0; padding: 0; }
  html, body { width: 1200px; height: 799px; overflow: hidden; }
  body {
    background: var(--backdrop);
    font-family: "Lato", sans-serif;
    position: relative;
  }
  .card {
    position: absolute;
    top: 238px;
    width: 500px;
    height: 324px;
    background: var(--card);
    border-radius: 3px;
    overflow: hidden;
  }
  .card--back { left: 70px; }
  .card--front { left: 630px; }

  .gloss-pattern {
    position: absolute;
    inset: 0;
    background: linear-gradient(120deg, var(--gloss-light) 0%, #3a3a3a 35%, var(--gloss-dark) 75%);
    opacity: 0.55;
  }
  .back-brand {
    position: absolute;
    left: 50%;
    top: 50%;
    transform: translate(-50%, -50%);
    display: flex;
    align-items: center;
    gap: 12px;
    background: var(--card);
    padding: 10px 16px;
  }
  .brand-square {
    width: 30px;
    height: 30px;
    background: var(--gold);
  }
  .brand-name {
    font-family: "Lato", sans-serif;
    font-weight: 700;
    color: var(--gold);
    letter-spacing: 0.18em;
    font-size: 26px;
  }

  .person {
    position: absolute;
    left: 34px;
    top: 108px;
  }
  .person-name {
    font-family: "Playfair Display", serif;
    font-weight: 400;
    color: var(--gold);
    font-size: 30px;
    line-height: 1;
  }
  .person-role {
    color: #d8d2c8;
    font-size: 13px;
    margin-top: 4px;
  }
  .front-brand {
    position: absolute;
    right: 34px;
    top: 92px;
    display: flex;
    flex-direction: column;
    align-items: center;
    gap: 12px;
  }
  .front-brand .brand-square { width: 62px; height: 62px; }
  .front-brand .brand-name { font-size: 28px; }
  .divider {
    position: absolute;
    left: 34px;
    right: 34px;
    top: 196px;
    height: 1px;
    background: var(--gold-dim);
  }
  .contacts {
    position: absolute;
    left: 34px;
    right: 34px;
    top: 214px;
    display: flex;
    justify-content: space-between;
    color: #e6e1d8;
    font-size: 12.5px;
    line-height: 1.9;
  }
  .contact-line { display: flex; align-items: center; gap: 8px; }
  .contact-line svg { width: 11px; height: 11px; fill: var(--gold); flex: none; }
  .contact-group--address .contact-line { align-items: flex-start; }
  .contact-group--address svg { margin-top: 5px; }
</style>
</head>
<body>
  <section class="card card--back" aria-label="Card back">
    <div class="gloss-pattern" role="img" aria-label="Repeating brand mark pattern in glossy black, fading from silver to black"></div>
    <div class="back-brand">
      <span class="brand-square"></span>
      <span class="brand-name">KELMONT</span>
    </div>
  </section>

  <section class="card card--front" aria-label="Card front">
    <div class="person">
      <h1 class="person-name">Ravi Dhillon</h1>
      <p class="person-role">Director</p>
    </div>
    <div class="front-brand">
      <span class="brand-square"></span>
      <span class="brand-name">KELMONT</span>
    </div>
    <div class="divider"></div>
    <div class="contacts">
      <div class="contact-group">
        <p class="contact-line"><svg viewBox="0 0 12 12"><path d="M2.5 1l2 2.2-1 1.3a7 7 0 0 0 4 4l1.3-1 2.2 2-1.2 1.5C5.5 11 1 6.5 1 2.2z"/></svg>0800 555 0142</p>
        <p class="contact-line"><svg viewBox="0 0 12 12"><path d="M3 0.5h6v11H3zM4 1.8v7.7h4V1.8z"/></svg>07700 900 318</p>
      </div>
      <div class="contact-group">
        <p class="contact-line"><svg viewBox="0 0 12 12"><path d="M0.5 2.5h11v7h-11zM1.5 3.3L6 6.5l4.5-3.2z"/></svg>ravi@kelmont.co.uk</p>
        <p class="contact-line"><svg viewBox="0 0 12 12"><circle cx="6" cy="6" r="5.5"/></svg>kelmont.co.uk</p>
      </div>
      <div class="contact-group contact-group--address">
        <p class="contact-line"><svg viewBox="0 0 12 12"><path d="M6 0.5a4 4 0 0 1 4 4c0 3-4 7-4 7s-4-4-4-7a4 4 0 0 1 4-4zm0 2.3a1.7 1.7 0 1 0 0 3.4 1.7 1.7 0 0 0 0-3.4z"/></svg><span>14 Millbrook Yard<br>Ashford TW15 3PL</span></p>
      </div>
    </div>
  </section>
</body>
</html>
```